Create a professional, eye-catching business card design that reflects the values and services of Brookfern Veterinary Hospital. we provide veterinary services and the business card should be a memorable representation of the clinic and align with its branding and mission. our tag line is "Faithful Friends, Thoughtful Care"
Use clean, modern typography. Prioritize readability and professionalism. We would like to see designs that use the color blue, as in the logo example. the final design should communicate professionalism and care, with attention to detail.

```html
<!DOCTYPE html>
<html lang="en">
<head>
<meta charset="utf-8">
<title>Brookfern Veterinary Hospital – Business Card</title>
<link href="https://fonts.googleapis.com/css2?family=Montserrat:wght@700&family=Lexend:wght@300;400&display=swap" rel="stylesheet">
<style>
  :root {
    --navy: #1d3461;
    --backdrop: #525858;
    --paper: #ffffff;
    --tint: #dfe5f0;
  }
  * { margin: 0; padding: 0; box-sizing: border-box; }
  html, body { width: 1200px; height: 1151px; overflow: hidden; }
  body { background: var(--backdrop); position: relative; font-family: "Lexend", sans-serif; }

  .card {
    position: absolute;
    left: 286px;
    width: 628px;
    height: 359px;
    border-radius: 24px;
    overflow: hidden;
    box-shadow: 10px 10px 10px rgba(0,0,0,0.75);
  }
  .card-front { top: 189px; background: var(--paper); color: var(--navy); }
  .card-back { top: 603px; background: var(--navy); color: var(--paper); }

  .front-wordmark {
    position: absolute; left: 32px; top: 31px;
    font-family: "Montserrat", sans-serif; font-weight: 700; color: var(--navy);
    line-height: 1;
  }
  .front-wordmark .brand-name { display: block; font-size: 44px; letter-spacing: 0.3px; }
  .front-wordmark .brand-sub { display: block; font-size: 15.5px; margin-top: -3px; letter-spacing: 0.5px; }

  .accent-bar {
    position: absolute; left: 0; top: 132px; width: 13px; height: 36px;
    background: var(--navy); border-radius: 0 5px 5px 0;
  }
  .person-name {
    position: absolute; left: 33px; top: 126px;
    font-family: "Montserrat", sans-serif; font-weight: 700; font-size: 23px; letter-spacing: 0.3px;
    line-height: 1.2;
  }
  .person-role { position: absolute; left: 33px; top: 154px; font-size: 16.5px; font-weight: 300; }

  .address { position: absolute; left: 33px; top: 198px; font-size: 16.5px; font-weight: 300; line-height: 23px; }

  .contact-list { position: absolute; left: 32px; top: 255px; list-style: none; }
  .contact-list li {
    display: flex; align-items: center; height: 25px;
    font-size: 16.5px; font-weight: 300;
  }
  .contact-list svg { width: 14px; height: 14px; margin-right: 7px; fill: var(--navy); flex: none; }

  .front-illustration {
    position: absolute; left: 320px; top: 146px; width: 308px; height: 213px;
    border-radius: 150px 150px 0 0;
    background: linear-gradient(180deg, var(--tint) 0%, #b7c3da 65%, var(--navy) 100%);
  }

  .back-illustration {
    position: absolute; left: 195px; top: 58px; width: 200px; height: 135px;
    border-radius: 100px 100px 0 0;
    background: linear-gradient(180deg, #2c4777 0%, #4a6394 70%, #c9d3e6 100%);
  }
  .back-wordmark {
    position: absolute; left: 0; right: 0; top: 194px; text-align: center;
    font-family: "Montserrat", sans-serif; font-weight: 700; color: var(--paper); line-height: 1;
  }
  .back-wordmark .brand-name { display: block; font-size: 56px; letter-spacing: 1px; }
  .back-wordmark .brand-sub { display: block; font-size: 19px; margin-top: -2px; letter-spacing: 0.8px; }
  .tagline {
    position: absolute; left: 0; right: 0; top: 312px; text-align: center;
    font-size: 17px; font-weight: 400; letter-spacing: 0.3px;
  }
</style>
</head>
<body>
  <section class="card card-front">
    <div class="front-wordmark">
      <span class="brand-name">BROOKFERN</span>
      <span class="brand-sub">VETERINARY HOSPITAL</span>
    </div>

    <div class="accent-bar"></div>
    <h1 class="person-name">DR. ELENA MARSH</h1>
    <p class="person-role">Founder &amp; CEO</p>

    <p class="address">1870 W Willow Ave<br>Fairmont, Arkansas, 72410</p>

    <ul class="contact-list">
      <li>
        <svg viewBox="0 0 24 24" aria-hidden="true"><path d="M6.6 10.8c1.4 2.8 3.8 5.1 6.6 6.6l2.2-2.2c.3-.3.7-.4 1-.2 1.1.4 2.3.6 3.6.6.6 0 1 .4 1 1V20c0 .6-.4 1-1 1C10.6 21 3 13.4 3 4c0-.6.4-1 1-1h3.5c.6 0 1 .4 1 1 0 1.3.2 2.5.6 3.6.1.3 0 .7-.2 1z"/></svg>
        (555) 214-3086
      </li>
      <li>
        <svg viewBox="0 0 24 24" aria-hidden="true"><path d="M2 5h20v14H2z M4 7v.4l8 5.6 8-5.6V7z" fill-rule="evenodd"/><path d="M4 7l8 5.6L20 7v1.5l-8 5.6-8-5.6z" fill="#fff"/></svg>
        info@brookfernvethospital.com
      </li>
      <li>
        <svg viewBox="0 0 24 24" aria-hidden="true"><path d="M12 2a10 10 0 1 0 0 20 10 10 0 0 0 0-20zm6.9 6h-3a15 15 0 0 0-1.3-3.9A8 8 0 0 1 18.9 8zM12 4c.9 1.2 1.5 2.6 1.9 4h-3.8c.4-1.4 1-2.8 1.9-4zM4.3 14a8 8 0 0 1 0-4h3.4a16 16 0 0 0 0 4zm.8 2h3a15 15 0 0 0 1.3 3.9A8 8 0 0 1 5.1 16zm3-8h-3a8 8 0 0 1 4.3-3.9C8.8 5.3 8.4 6.6 8.1 8zM12 20c-.9-1.2-1.5-2.6-1.9-4h3.8c-.4 1.4-1 2.8-1.9 4zm2.3-6H9.7a14 14 0 0 1 0-4h4.6a14 14 0 0 1 0 4zm.3 5.9c.6-1.2 1-2.5 1.3-3.9h3a8 8 0 0 1-4.3 3.9zM16.3 14a16 16 0 0 0 0-4h3.4a8 8 0 0 1 0 4z"/></svg>
        brookfernvethospital.com
      </li>
    </ul>

    <div class="front-illustration" role="img" aria-label="Navy illustration area: a cat and a dog sitting on a hill inside a circle under a leafy branch"></div>
  </section>

  <section class="card card-back">
    <div class="back-illustration" role="img" aria-label="White illustration area: a cat and a dog sitting on a hill inside a circle under a leafy branch"></div>
    <div class="back-wordmark">
      <span class="brand-name">BROOKFERN</span>
      <span class="brand-sub">VETERINARY HOSPITAL</span>
    </div>
    <p class="tagline">Faithful Friends, Thoughtful Care</p>
  </section>
</body>
</html>
```